Pemberton Dialworks Business Card Design

Double Sided Business Card Design for a Locksmith company specializing in Safecracking, safe & vault service.

```html
<!DOCTYPE html>
<html lang="en">
<head>
<meta charset="utf-8">
<title>Pemberton Dialworks Business Card</title>
<link href="https://fonts.googleapis.com/css2?family=Montserrat:ital,wght@0,400;0,600;0,800;1,400&display=swap" rel="stylesheet">
<style>
  :root {
    --green: #2e8b3a;
    --green-dark: #237030;
    --ink: #1f1f1f;
    --black-card: #242424;
    --grey-block: #8a8a8a;
    --text-grey: #6a6a6a;
    --page: #e9eaec;
    --white: #ffffff;
  }
  * { margin: 0; padding: 0; box-sizing: border-box; }
  html, body { width: 1200px; height: 800px; overflow: hidden; }
  body {
    background: var(--page);
    font-family: "Montserrat", Arial, sans-serif;
    position: relative;
  }
  .card {
    position: absolute;
    top: 245px;
    width: 540px;
    height: 309px;
    overflow: hidden;
    border-radius: 3px;
    box-shadow: 0 6px 20px rgba(0,0,0,0.18);
  }
  .card--front { left: 40px; background: var(--white); }
  .card--back { left: 620px; background: radial-gradient(ellipse at 45% 40%, #3a3a3a 0%, var(--black-card) 70%); }

  .pattern-area { position: absolute; }
  .card--front .pattern-area {
    left: 0; top: 0; width: 540px; height: 150px;
    background: linear-gradient(180deg, #ececec 0%, #f6f6f6 60%, rgba(255,255,255,0) 100%);
  }
  .card--back .pattern-area {
    right: 0; top: 0; width: 260px; height: 190px;
    background: radial-gradient(ellipse at 70% 40%, rgba(255,255,255,0.06), rgba(255,255,255,0) 70%);
  }

  .bands { position: absolute; left: 0; top: 0; }

  .brand { position: absolute; display: flex; align-items: center; gap: 12px; }
  .brand__dot { border-radius: 50%; background: var(--green); flex: none; }
  .brand__name {
    font-weight: 800;
    text-transform: uppercase;
    line-height: 1.02;
    letter-spacing: 0.5px;
  }
  .card--front .brand { left: 148px; top: 52px; }
  .card--front .brand__dot { width: 58px; height: 58px; }
  .card--front .brand__name { font-size: 23px; color: var(--green); }
  .card--back .brand { left: 120px; top: 80px; }
  .card--back .brand__dot { width: 84px; height: 84px; }
  .card--back .brand__name { font-size: 34px; color: var(--white); }

  .contact { position: absolute; left: 268px; top: 126px; color: var(--ink); }
  .contact__row { display: flex; align-items: center; gap: 10px; font-size: 11.5px; height: 22px; }
  .contact__row b { font-weight: 800; }
  .contact__label { font-size: 11.5px; margin-top: 4px; color: #333; }
  .contact__phone { display: flex; align-items: center; gap: 10px; margin-top: 4px; }
  .contact__number { font-size: 22px; font-weight: 800; letter-spacing: 4px; white-space: nowrap; }
  .contact__number .dash { color: var(--green); }
  .icon { width: 16px; height: 16px; flex: none; }

  .holder { position: absolute; left: 26px; top: 214px; }
  .holder__icon { width: 16px; height: 16px; display: block; margin-bottom: 4px; }
  .holder__text { font-size: 15px; color: var(--text-grey); text-transform: uppercase; white-space: nowrap; }
  .holder__text strong { color: var(--green); font-weight: 800; }
  .holder__rule { width: 230px; height: 2px; background: linear-gradient(90deg, #999 0 70%, var(--green) 70% 100%); margin-top: 3px; }

  .callout {
    position: absolute; left: 60px; top: 198px;
    font-size: 15px; font-style: italic; color: #cfcfcf;
  }
  .callout__phone { color: var(--green); font-style: normal; font-weight: 800; margin-left: 6px; }
</style>
</head>
<body>

<section class="card card--front" aria-label="Business card front">
  <div class="pattern-area" role="img" aria-label="Light grey hexagonal cube pattern"></div>
  <svg class="bands" width="540" height="309" viewBox="0 0 540 309" aria-hidden="true">
    <polygon points="405,242 540,242 540,266 390,266" fill="var(--grey-block)"/>
    <polygon points="0,292 370,266 540,266 540,309 0,309" fill="var(--green)"/>
  </svg>

  <div class="brand">
    <span class="brand__dot"></span>
    <span class="brand__name">Pemberton<br>Dialworks</span>
  </div>

  <div class="contact">
    <div class="contact__row">
      <svg class="icon" viewBox="0 0 16 16" aria-hidden="true"><path d="M1 8 L15 2 L10 14 L7 9 Z M7 9 L15 2" fill="none" stroke="var(--green)" stroke-width="1.3" stroke-linejoin="round"/></svg>
      <span>info@<b>pembertondialworks</b>.com</span>
    </div>
    <div class="contact__row">
      <svg class="icon" viewBox="0 0 16 16" aria-hidden="true"><circle cx="8" cy="8" r="6.5" fill="none" stroke="var(--green)" stroke-width="1.3"/><ellipse cx="8" cy="8" rx="3" ry="6.5" fill="none" stroke="var(--green)" stroke-width="1.1"/><line x1="1.5" y1="8" x2="14.5" y2="8" stroke="var(--green)" stroke-width="1.1"/></svg>
      <span>www.<b>pembertondialworks</b>.com</span>
    </div>
    <div class="contact__label">Free Phone Consultation &amp; Estimate:</div>
    <div class="contact__phone">
      <svg class="icon" viewBox="0 0 16 16" aria-hidden="true"><path d="M4 2 L6.5 5 L5 6.8 C6 9 7.2 10.2 9.2 11 L11 9.5 L14 12 L12.5 14 C7 13.5 2.5 9 2 3.5 Z" fill="none" stroke="var(--green)" stroke-width="1.3" stroke-linejoin="round"/></svg>
      <span class="contact__number">555<span class="dash">-</span>014<span class="dash">-</span>2276</span>
    </div>
  </div>

  <div class="holder">
    <svg class="holder__icon" viewBox="0 0 16 16" aria-hidden="true"><circle cx="8" cy="5" r="3.2" fill="none" stroke="var(--green)" stroke-width="1.3"/><path d="M2 15 C2 10.5 14 10.5 14 15" fill="none" stroke="var(--green)" stroke-width="1.3"/></svg>
    <div class="holder__text"><strong>Your Name</strong>, Designation</div>
    <div class="holder__rule"></div>
  </div>
</section>

<section class="card card--back" aria-label="Business card back">
  <div class="pattern-area" role="img" aria-label="Faint dark hexagonal pattern"></div>
  <svg class="bands" width="540" height="309" viewBox="0 0 540 309" aria-hidden="true">
    <polygon points="0,205 460,282 450,300 0,228" fill="var(--green)"/>
    <polygon points="460,282 540,282 540,309 445,309" fill="var(--grey-block)"/>
  </svg>

  <div class="brand">
    <span class="brand__dot"></span>
    <span class="brand__name">Pemberton<br>Dialworks</span>
  </div>

  <p class="callout">Call now for free estimate!<span class="callout__phone">555-014-2276</span></p>
</section>

</body>
</html>
```